Need Business cards

Im a new realtor and already have a logo. I would like to purchase a Business card design that catches customer's attention, its creative, and modern.

Marisol Vandera
Realtor ®
(555) 214 7730
marisolvndrealtor@brightmailbox.com

Target Market(s)

investors, buyers and seller, property management

Industry/Entity Type

real estate,

Contact Information for Business Card

Marisol Vandera

Requirements
Must have
• BOTH LOGOS, WOULD LIKE TO SEE WITH DIFFERENT OPTIONS WITH EITHER PICTURE

```html
<!DOCTYPE html>
<html lang="en">
<head>
<meta charset="utf-8">
<title>Marisol Vandera — Realtor Business Cards</title>
<link href="https://fonts.googleapis.com/css2?family=Montserrat:wght@600;700&family=Barlow:wght@400;500;600&display=swap" rel="stylesheet">
<style>
  :root {
    --stage: #2b2b2b;
    --navy-top: #0c2150;
    --navy-bottom: #03173d;
    --card-dark: #1c1c1c;
    --gold: #c9a22e;
    --gold-soft: #b8912a;
    --white: #f2f2f2;
    --grey-text: #d8d8d8;
    --brand-blue: #3a7fd6;
    --photo-a: #3a3129;
    --photo-b: #8a6c4e;
  }
  * { box-sizing: border-box; margin: 0; padding: 0; }
  html, body {
    width: 1200px; height: 1138px; overflow: hidden;
    background: var(--stage);
  }
  .canvas { position: relative; width: 1200px; height: 1138px; }

  .card {
    position: absolute;
    border-radius: 14px;
    overflow: hidden;
  }

  /* Front card */
  .card-front {
    left: 274px; top: 186px; width: 623px; height: 374px;
    background: linear-gradient(160deg, var(--navy-top), var(--navy-bottom));
  }
  .front-lockup {
    position: absolute; left: 0; right: 0; top: 150px;
    text-align: center;
    font-family: "Montserrat", sans-serif;
    color: var(--gold);
  }
  .front-lockup .brand-name {
    display: inline-flex; align-items: center; gap: 14px;
    font-size: 34px; font-weight: 700; letter-spacing: 0.5px;
  }
  .brand-square {
    display: inline-block; width: 22px; height: 22px;
    background: var(--gold);
  }
  .front-lockup .brand-role {
    display: flex; align-items: center; justify-content: center; gap: 8px;
    margin-top: 10px;
    font-size: 16px; font-weight: 600; letter-spacing: 1px;
  }
  .front-lockup .brand-role::before,
  .front-lockup .brand-role::after {
    content: ""; width: 64px; height: 1px; background: var(--gold);
  }

  /* Back card */
  .card-back {
    left: 276px; top: 608px; width: 618px; height: 372px;
    background: var(--card-dark);
  }
  .back-lockup {
    position: absolute; left: 44px; top: 56px;
    font-family: "Montserrat", sans-serif;
    color: var(--gold);
  }
  .back-lockup .brand-name {
    display: flex; align-items: center; gap: 12px;
    font-size: 24px; font-weight: 700; letter-spacing: 0.4px;
  }
  .back-lockup .brand-square { width: 18px; height: 18px; }
  .back-lockup .brand-role {
    display: flex; align-items: center; gap: 6px;
    margin-top: 6px; margin-left: 30px;
    font-size: 15px; font-weight: 600; letter-spacing: 0.8px;
  }
  .back-lockup .brand-role::before,
  .back-lockup .brand-role::after {
    content: ""; width: 76px; height: 1px; background: var(--gold);
  }

  .portrait {
    position: absolute; left: 402px; top: 14px; width: 216px; height: 246px;
    background: linear-gradient(180deg, var(--photo-b) 0%, var(--photo-a) 70%, #161616 100%);
  }

  .agent {
    position: absolute; left: 44px; top: 212px;
    font-family: "Barlow", sans-serif;
  }
  .agent-name { font-size: 27px; font-weight: 600; color: var(--white); line-height: 1.1; }
  .agent-title { font-size: 14px; font-weight: 500; color: var(--gold); margin-top: 4px; }
  .divider {
    position: absolute; left: 118px; right: 0; top: 259px;
    height: 2px; background: var(--gold-soft);
  }

  .contact {
    position: absolute; left: 44px; top: 296px;
    list-style: none;
    font-family: "Barlow", sans-serif; font-size: 14.5px; color: var(--grey-text);
  }
  .contact li { display: flex; align-items: center; gap: 14px; height: 26px; }
  .contact svg { width: 16px; height: 14px; fill: var(--gold); }

  .brokerage {
    position: absolute; right: 36px; top: 310px;
    display: flex; align-items: center; gap: 8px;
    font-family: "Barlow", sans-serif; font-size: 19px; font-weight: 600;
    letter-spacing: 0.6px; color: var(--brand-blue);
  }
  .brokerage .mark { width: 12px; height: 12px; background: var(--brand-blue); }
</style>
</head>
<body>
<main class="canvas">
  <section class="card card-front" aria-label="Business card front">
    <div class="front-lockup">
      <div class="brand-name"><span class="brand-square"></span>MARISOL VANDERA</div>
      <div class="brand-role">REALTOR</div>
    </div>
  </section>

  <section class="card card-back" aria-label="Business card back">
    <div class="back-lockup">
      <div class="brand-name"><span class="brand-square"></span>MARISOL VANDERA</div>
      <div class="brand-role">REALTOR</div>
    </div>

    <div class="portrait" role="img" aria-label="Portrait photo of the realtor"></div>

    <div class="agent">
      <div class="agent-name">Marisol Vandera</div>
      <div class="agent-title">Realtor®</div>
    </div>
    <div class="divider"></div>

    <ul class="contact">
      <li>
        <svg viewBox="0 0 16 14" aria-hidden="true"><path d="M1 4c0-2 3-3 7-3s7 1 7 3v1h-4V3.5H5V5H1z M3 7h10l1 6H2z M6 9h4v2H6z"/></svg>
        (555) 214 7730
      </li>
      <li>
        <svg viewBox="0 0 16 14" aria-hidden="true"><path d="M1 2h14v10H1z M2 3l6 5 6-5" stroke="#1c1c1c" stroke-width="1.2"/></svg>
        marisolvndrealtor@brightmailbox.com
      </li>
    </ul>

    <div class="brokerage"><span class="mark"></span>ASCENTRA REALTY</div>
  </section>
</main>
</body>
</html>
```